Commercial snow and summer maintenance marketing folders

I'M looking to design a marketing folder for my snow and summer maintenance company.
The folder is a 12''x9'' , i want to fill up the front and back.
Acquire them for the first,keep them for all time is the slogan that will go somewhere in the front ,
I will attach logo, im thinking to having that in the front,top,middle. having a small logo in back bottom middle of page with phone number 647-319-5520,www.brindlegrounds.com . Proud members of Greenway Guild, Wise With Grit And TCPA with small logos beside them. Small writing underneath "2016 Brindle Grounds Ltd. Independently owned and operated. Propriety and Confidential
B2B, Industrial, commercial and municipal customers
Snow Removal

```html
<!DOCTYPE html>
<html lang="en">
<head>
<meta charset="utf-8">
<title>Brindle Grounds – Marketing Folder</title>
<link href="https://fonts.googleapis.com/css2?family=Roboto+Condensed:wght@400;700&family=Roboto:wght@400;500&display=swap" rel="stylesheet">
<style>
  :root {
    --green: #6cb52d;
    --dark: #3b3b3b;
    --blue: #2a9fd6;
    --pocket: #8ccbe9;
    --band: #dceefa;
    --mist: #f5f6f5;
    --page: #e9eaeb;
    --ink: #444;
  }
  * { box-sizing: border-box; margin: 0; padding: 0; }
  html, body { width: 960px; height: 1200px; overflow: hidden; background: var(--page); }
  body { font-family: "Roboto", Arial, sans-serif; color: var(--ink); }
  .spread { position: absolute; left: 50px; width: 860px; height: 573px; display: flex; box-shadow: 0 4px 18px rgba(0,0,0,.18); background: #fff; }
  .spread--outside { top: 18px; }
  .spread--inside { top: 609px; }
  .panel { position: relative; width: 430px; height: 573px; overflow: hidden; background: #fff; }
  .panel svg.shapes { position: absolute; inset: 0; }
  .brand { position: absolute; left: 0; right: 0; display: flex; align-items: center; justify-content: center; gap: 8px; font-family: "Roboto Condensed", Arial, sans-serif; font-weight: 700; color: var(--dark); letter-spacing: 3px; }
  .brand__mark { width: 12px; height: 12px; background: var(--green); }
  .brand--large { font-size: 26px; }
  .brand--small { font-size: 13px; letter-spacing: 2px; }
  .brand--small .brand__mark { width: 8px; height: 8px; }
  .brand--ghost { color: #e8ece6; font-size: 36px; letter-spacing: 6px; }
  .contact { position: absolute; left: 0; right: 0; text-align: center; font-size: 11px; line-height: 17px; color: var(--ink); }
  .contact .icon { display: inline-block; width: 8px; height: 8px; border-radius: 50%; background: var(--blue); margin-right: 4px; vertical-align: 0; }
  .slogan { position: absolute; left: 0; right: 0; top: 232px; text-align: center; font-family: "Roboto Condensed", Arial, sans-serif; font-weight: 700; line-height: 1.2; }
  .slogan__line--blue { color: var(--blue); }
  .slogan__line--green { color: var(--green); }
  .slogan__line--sm { font-size: 25px; }
  .slogan__line--lg { font-size: 42px; line-height: 1.05; }
  .slogan__gap { height: 14px; }
  .members-band { position: absolute; left: 0; right: 0; top: 262px; height: 42px; background: var(--band); color: var(--blue); font-size: 26px; display: flex; align-items: center; justify-content: center; }
  .member { position: absolute; display: flex; align-items: center; gap: 7px; font-family: "Roboto", Arial, sans-serif; font-weight: 500; color: var(--dark); }
  .member__mark { width: 14px; height: 14px; background: var(--dark); }
  .member--guild { left: 74px; top: 352px; font-size: 24px; }
  .member--guild .member__mark { width: 26px; height: 26px; border-radius: 50%; }
  .member--grit { left: 70px; top: 424px; font-size: 17px; }
  .member--grit .member__mark { background: var(--blue); border-radius: 50%; width: 10px; height: 10px; }
  .member--tcpa { left: 250px; top: 420px; font-size: 24px; font-weight: 500; }
  .legal { position: absolute; left: 70px; right: 70px; top: 500px; text-align: center; font-size: 8px; line-height: 11px; color: #555; }
  .foot-strip { position: absolute; left: 0; right: 0; bottom: 0; height: 12px; background: #e6f3fb; }
</style>
</head>
<body>

<section class="spread spread--outside">
  <!-- back cover -->
  <div class="panel panel--back">
    <svg class="shapes" width="430" height="573" viewBox="0 0 430 573">
      <defs>
        <radialGradient id="grassGlow" cx="50%" cy="60%" r="55%">
          <stop offset="0" stop-color="#e4efdc"/>
          <stop offset="1" stop-color="#f5f6f5" stop-opacity="0"/>
        </radialGradient>
      </defs>
      <polygon points="0,0 430,0 430,440 215,378 0,440" fill="var(--mist)"/>
      <rect x="50" y="130" width="300" height="160" fill="url(#grassGlow)" role="img" aria-label="Faint grass tuft with falling snowflakes"/>
      <polygon points="0,440 215,378 430,440 430,449 215,387 0,449" fill="var(--green)"/>
      <polyline points="0,459 215,397 430,459" fill="none" stroke="var(--dark)" stroke-width="3"/>
    </svg>
    <div class="brand brand--small" style="top:458px"><span class="brand__mark"></span>BRINDLE GROUNDS</div>
    <div class="contact" style="top:495px">
      <div><span class="icon"></span>www.brindlegrounds.com</div>
      <div><span class="icon"></span>647-319-5520</div>
    </div>
  </div>

  <!-- front cover -->
  <div class="panel panel--front">
    <svg class="shapes" width="430" height="573" viewBox="0 0 430 573">
      <polygon points="0,150 215,200 430,150 430,530 215,488 0,530" fill="var(--mist)"/>
      <polygon points="215,185 345,245 345,400 215,460 85,400 85,245" fill="none" stroke="#e7efe3" stroke-width="14" stroke-linejoin="round"/>
      <polygon points="0,135 215,185 430,135 430,144 215,194 0,144" fill="var(--green)"/>
      <polyline points="0,152 215,202 430,152" fill="none" stroke="var(--dark)" stroke-width="3"/>
      <polygon points="0,520 215,478 430,520 430,529 215,487 0,529" fill="var(--green)"/>
      <polyline points="0,537 215,495 430,537" fill="none" stroke="var(--dark)" stroke-width="3"/>
    </svg>
    <div class="brand brand--large" style="top:72px"><span class="brand__mark"></span>BRINDLE GROUNDS</div>
    <div class="slogan">
      <div class="slogan__line--blue slogan__line--sm">ACQUIRE THEM</div>
      <div class="slogan__line--green slogan__line--sm">FOR THE FIRST</div>
      <div class="slogan__gap"></div>
      <div class="slogan__line--blue slogan__line--lg">KEEP THEM</div>
      <div class="slogan__line--green slogan__line--lg">FOR ALL TIME</div>
    </div>
    <div class="contact" style="top:546px"><span class="icon"></span>www.brindlegrounds.com</div>
  </div>
</section>

<section class="spread spread--inside">
  <!-- inside left -->
  <div class="panel panel--inside-left">
    <svg class="shapes" width="430" height="573" viewBox="0 0 430 573">
      <defs>
        <linearGradient id="winterPhoto" x1="0" y1="0" x2="1" y2="1">
          <stop offset="0" stop-color="#cfd6dc"/>
          <stop offset=".5" stop-color="#d98b4a"/>
          <stop offset="1" stop-color="#b9c2c9"/>
        </linearGradient>
      </defs>
      <polygon points="0,0 430,0 430,140 215,200 0,140" fill="url(#winterPhoto)" role="img" aria-label="Photo of a snow crew worker in a hard hat and high-visibility vest holding a shovel"/>
      <polygon points="0,146 215,206 430,146 430,155 215,215 0,155" fill="var(--green)"/>
      <polyline points="0,163 215,223 430,163" fill="none" stroke="var(--dark)" stroke-width="3"/>
    </svg>
    <div class="members-band">Proud Members Of</div>
    <div class="member member--guild"><span class="member__mark"></span>Greenway Guild</div>
    <div class="member member--grit"><span class="member__mark"></span>Wise With Grit</div>
    <div class="member member--tcpa"><span class="member__mark"></span>TCPA</div>
    <p class="legal">2016 Brindle Grounds Ltd. Independently owned and operated. Propriety and Confidential</p>
    <div class="foot-strip"></div>
  </div>

  <!-- inside right with pocket -->
  <div class="panel panel--inside-right">
    <svg class="shapes" width="430" height="573" viewBox="0 0 430 573">
      <defs>
        <linearGradient id="lawnPhoto" x1="0" y1="0" x2="0" y2="1">
          <stop offset="0" stop-color="#a9c48a"/>
          <stop offset="1" stop-color="#6f9a45"/>
        </linearGradient>
      </defs>
      <polygon points="0,0 430,0 430,125 215,180 0,125" fill="url(#lawnPhoto)" role="img" aria-label="Photo of a lawn mower being pushed across green grass"/>
      <polygon points="0,131 215,186 430,131 430,140 215,195 0,140" fill="var(--green)"/>
      <polyline points="0,148 215,203 430,148" fill="none" stroke="var(--dark)" stroke-width="3"/>
      <polygon points="0,410 215,348 430,410 430,419 215,357 0,419" fill="var(--green)"/>
      <polyline points="0,426 215,364 430,426" fill="none" stroke="var(--dark)" stroke-width="3"/>
      <polygon points="0,436 215,374 430,436 430,573 0,573" fill="var(--pocket)"/>
    </svg>
    <div class="brand brand--ghost" style="top:262px">BRINDLE GROUNDS</div>
    <div class="brand brand--large" style="top:480px"><span class="brand__mark"></span>BRINDLE GROUNDS</div>
  </div>
</section>

</body>
</html>
```